Tea box package for Herbal Teas

We would like a design for a package of our tea products. We want the consumer to understand that our products are natural just by looking at the package. We prefer minimalistic designs.
The package we want would be a square (or slightly rectangular) box. The box would be generic enough for us to use it for different teas. Essentially what we want is all the main information and designs to be the same for each tea product we have. We would like to be able to change the main color and the name of the tea then to customize to the tea in the package. Please see the attached images for examples.
We really like the package in tea_packaging_example_4 picture. We would like our packaging to be something very similar but with all the labels printed on the package.
We already have our logo so I am attaching that as well (image named 'velka brin logo copy'). That would go on the front of the box.
We also attach a tile created using our logo (see image called 'tile'). We would like this to go to the sides similarly to tea_packaging_example_4.
On the back of the pouch, we want to have directions on how to make the tea but we want this section to be editable. For now just 3-4 lines of sample text is fine along with instructions on how to make a tea, see picture 'back of tea box'.
We would like for the box color to be as in example picture
tea_packaging_example_4. The color of the writing should be the same as the logo color. The font style should be something that would look nice next to the logo font, we are not sure what that font should be. The only thing colored would be the name of the tea and the ribbon as seen in tea_packaging_example_4, which we would like to change if we need to, to other variations.
Thanks a lot. For any questions, please contact me.

```html
<!DOCTYPE html>
<html lang="en">
<head>
<meta charset="utf-8">
<title>Velka Brin – Tea Box Dieline</title>
<link href="https://fonts.googleapis.com/css2?family=Cormorant+Garamond:wght@500&family=Montserrat:wght@500;700;800&display=swap" rel="stylesheet">
<style>
  :root {
    --paper: #ffffff;
    --cut: #e5197a;
    --fold: #3aa757;
    --label: #b2b47e;
    --pattern: #cfd0a6;
    --ink: #3a3a3c;
    --ribbon: #ede57b;
  }
  html, body {
    margin: 0;
    padding: 0;
    width: 1200px;
    height: 870px;
    overflow: hidden;
    background: var(--paper);
  }
  .dieline { display: block; width: 1200px; height: 870px; }
  .spec { font-family: "Montserrat", sans-serif; font-weight: 500; font-size: 20px; fill: #111; }
  .cut { fill: none; stroke: var(--cut); stroke-width: 1.4; }
  .fold { fill: none; stroke: var(--fold); stroke-width: 1.2; stroke-dasharray: 7 5; }
  .label-panel { fill: var(--label); }
  .side-pattern { fill: var(--pattern); }
  .ribbon { fill: var(--ribbon); }
  .brand-mark { fill: var(--ink); }
  .brand-name { font-family: "Cormorant Garamond", serif; font-weight: 500; fill: var(--ink); text-anchor: middle; }
  .kicker { font-family: "Montserrat", sans-serif; font-weight: 700; font-size: 7px; letter-spacing: 3.4px; fill: var(--ink); text-anchor: middle; }
  .tea-name { font-family: "Montserrat", sans-serif; font-weight: 800; font-size: 17px; letter-spacing: 2.6px; fill: var(--ink); text-anchor: middle; }
  .tea-notes { font-family: "Montserrat", sans-serif; font-weight: 800; font-size: 5.4px; letter-spacing: 2.6px; fill: var(--ink); text-anchor: middle; }
  .count { font-family: "Montserrat", sans-serif; font-weight: 700; font-size: 15px; fill: #111; text-anchor: middle; }
  .count-caption { font-family: "Montserrat", sans-serif; font-weight: 800; font-size: 7px; letter-spacing: 4.6px; fill: #111; text-anchor: middle; }
  .copy { font-family: "Montserrat", sans-serif; font-weight: 700; font-size: 5.3px; letter-spacing: 0.3px; fill: var(--ink); text-anchor: middle; }
  .step-title { font-family: "Montserrat", sans-serif; font-weight: 700; font-size: 5.5px; fill: var(--ink); text-anchor: middle; }
  .step-detail { font-family: "Montserrat", sans-serif; font-weight: 500; font-size: 3.8px; fill: var(--ink); text-anchor: middle; }
  .icon { fill: none; stroke: var(--ink); stroke-width: 2; stroke-linejoin: round; stroke-linecap: round; }
  .icon-solid { fill: var(--ink); }
  .divider { stroke: var(--ink); stroke-width: 0.8; }
  .social-dot { fill: none; stroke: var(--ink); stroke-width: 1.3; }
</style>
</head>
<body>
<svg class="dieline" viewBox="0 0 1500 1087.5" xmlns="http://www.w3.org/2000/svg">
  <text class="spec" x="30" y="52">Height 72mm x Width 85mm x Depth 68mm</text>

  <!-- Side panel patterns -->
  <rect class="side-pattern" x="107" y="463" width="288" height="305" role="img" aria-label="Repeating tile pattern of the brand emblem in olive on white"/>
  <rect class="side-pattern" x="755" y="463" width="288" height="305" role="img" aria-label="Repeating tile pattern of the brand emblem in olive on white"/>

  <!-- Cut lines -->
  <g class="cut-lines">
    <path class="cut" d="M107 463 L127 330 L375 330 L395 463"/>
    <path class="cut" d="M395 463 L755 463"/>
    <path class="cut" d="M755 463 L775 330 L1023 330 L1043 463"/>
    <path class="cut" d="M1043 463 L1043 175 L1068 108 L1380 108 L1403 175 L1403 463"/>
    <path class="cut" d="M107 463 L107 901 L279 901 L279 870 L251 870 L251 846 L395 768"/>
    <path class="cut" d="M395 768 L395 970 L520 970 L520 932 L500 932 L500 883 L650 883 L650 932 L634 932 L634 970 L755 970 L755 768"/>
    <path class="cut" d="M755 768 L893 840 L893 870 L871 870 L871 901 L1043 901 L1043 768"/>
    <path class="cut" d="M1043 901 L1157 901 L1157 970 L1290 970 L1290 903 L1403 903 L1403 463"/>
  </g>

  <!-- Fold lines -->
  <g class="fold-lines">
    <path class="fold" d="M107 463 L395 463"/>
    <path class="fold" d="M755 463 L1403 463"/>
    <path class="fold" d="M1043 175 L1403 175"/>
    <path class="fold" d="M107 768 L1403 768"/>
    <path class="fold" d="M107 463 L107 768"/>
    <path class="fold" d="M395 463 L395 768"/>
    <path class="fold" d="M755 463 L755 768"/>
    <path class="fold" d="M1043 463 L1043 768"/>
  </g>

  <!-- Front panel -->
  <g class="front-panel">
    <rect class="label-panel" x="480" y="463" width="190" height="201"/>
    <text class="kicker" x="575" y="479">ORGANIC HERBAL TEA</text>
    <circle class="brand-mark" cx="575" cy="550" r="44"/>
    <text class="brand-name" x="575" y="633" font-size="23">VELKA BRIN</text>
    <rect class="ribbon" x="480" y="672" width="190" height="44"/>
    <text class="tea-name" x="575" y="691">REVERIE</text>
    <text class="tea-notes" x="575" y="701">WHITE BLOSSOM</text>
    <text class="tea-notes" x="575" y="709">CHAMOMILE</text>
    <text class="count" x="573" y="741">12</text>
    <text class="count-caption" x="575" y="753">HANDCRAFTED TEA BALLS</text>
  </g>

  <!-- Lid -->
  <g class="lid-panel">
    <rect class="label-panel" x="1128" y="175" width="190" height="288"/>
    <g transform="rotate(180 1224 300)">
      <text class="brand-name" x="1224" y="357" font-size="22">VELKA BRIN</text>
      <circle class="brand-mark" cx="1224" cy="275" r="52"/>
    </g>
  </g>

  <!-- Back panel -->
  <g class="back-panel">
    <rect class="label-panel" x="1128" y="463" width="190" height="305"/>
    <circle class="brand-mark" cx="1224" cy="510" r="27"/>
    <text class="brand-name" x="1224" y="559" font-size="13">VELKA BRIN</text>

    <text class="copy" x="1224" y="582">LOREM IPSUM DOLOR SIT AMET, CONSEC</text>
    <text class="copy" x="1224" y="589">TETUER ADIPISCING ELIT, SED DIAM</text>
    <text class="copy" x="1224" y="596">NONUMMY NIBH EUISMOD TINCIDUNT UT</text>
    <text class="copy" x="1224" y="603">LAOREET DOLORE MAGNA ALIQUAM ERAT</text>
    <text class="copy" x="1224" y="616">LOREM IPSUM DOLOR SIT AMET, CONSEC</text>
    <text class="copy" x="1224" y="623">TETUER ADIPISCING ELIT, SED DIAM</text>
    <text class="copy" x="1224" y="630">NONUMMY NIBH EUISMOD TINCIDUNT UT</text>
    <text class="copy" x="1224" y="637">LAOREET DOLORE MAGNA ALIQUAM ERAT</text>

    <g class="brew-steps">
      <path class="icon" d="M1166 663 L1176 655 L1190 663 L1190 681 L1166 681 Z"/>
      <path class="icon" d="M1176 655 L1160 668"/>
      <rect class="icon-solid" x="1156" y="667" width="7" height="7"/>
      <path class="icon-solid" d="M1168 672 L1188 672 L1188 679 L1168 679 Z"/>

      <path class="icon-solid" d="M1214 666 Q1226 658 1238 666 L1236 677 Q1226 682 1216 677 Z"/>
      <path class="icon" d="M1238 668 Q1245 667 1243 674 L1237 676"/>
      <path class="icon" d="M1214 668 L1207 664"/>
      <circle class="icon-solid" cx="1226" cy="661" r="2"/>

      <circle class="icon" cx="1271" cy="669" r="11"/>
      <path class="icon" d="M1271 662 L1271 670 L1276 673"/>

      <line class="divider" x1="1203" y1="688" x2="1203" y2="701"/>
      <line class="divider" x1="1248" y1="688" x2="1248" y2="701"/>

      <text class="step-title" x="1179" y="694">TEA</text>
      <text class="step-detail" x="1179" y="700">1 PER PERSON</text>
      <text class="step-title" x="1226" y="694">WATER</text>
      <text class="step-detail" x="1226" y="700">80°C</text>
      <text class="step-title" x="1271" y="694">BREW</text>
      <text class="step-detail" x="1271" y="700">3-5 MINUTES</text>
    </g>

    <text class="copy" x="1224" y="716">LOREM IPSUM DOLOR SIT AMET, CONSEC</text>
    <text class="copy" x="1224" y="723">TETUER ADIPISCING ELIT, SED DIAM</text>

    <circle class="social-dot" cx="1192" cy="744" r="8.5"/>
    <circle class="social-dot" cx="1224" cy="744" r="8.5"/>
    <circle class="social-dot" cx="1256" cy="744" r="8.5"/>
  </g>
</svg>
</body>
</html>
```